Various Design Assets for an Email Signature Template

I want to create a uniform email signature design for all users in my office. We utilize a cloud-based email signature platform called parlowen - I need to add the assets to my account, and they will deploy across all users. I want the design to include the following:
1 - A banner ad below my logo and the same size. Please design an advertisement to contact us for additional insurance, risk management, compliance, and financial services. I will add the link from my end.
2 - 4 'boxes,' which, in total, are the same size as the banner ad. I want the boxes designed for:
a - Subscribe to our vidorbit channel
b - listen to our podcast
c - book on our calendar
d - request a certificate of insurance
3 - The last asset below the two above is a social media strip for Chatterlane, Pixelnook, Workhive, and Quibbl.
Please let me know if you need our brand colors. Our website is kelvarisk.com.
Thank you!
Doran

Target Market(s)

Small to medium-sized business owners

Industry/Entity Type

Insurance Broker

Font styles to use
Other font styles liked:
• Ginto Nord

Requirements
Must have
• Design elements that match my brand.
Nice to have
• Call to action to gain the attention of our email recipients.

```html
<!DOCTYPE html>
<html lang="en">
<head>
<meta charset="utf-8">
<title>Contact Us Banner</title>
<link rel="stylesheet" href="https://fonts.googleapis.com/css2?family=Bebas+Neue&display=swap">
<style>
  :root {
    --charcoal: #32373a;
    --lime: #97b500;
    --white: #ffffff;
  }
  html, body {
    margin: 0;
    padding: 0;
    width: 1200px;
    height: 325px;
    overflow: hidden;
    background: var(--white);
  }
  .contact-banner {
    display: block;
    width: 1200px;
    height: 325px;
  }
  .banner-shape { fill: var(--charcoal); }
  .headline-band { fill: var(--lime); }
  .icon-disc { fill: var(--white); }
  .icon-swoosh {
    fill: none;
    stroke: var(--white);
    stroke-width: 14;
    stroke-linecap: round;
  }
  .phone-icon { fill: var(--charcoal); }
  .banner-text {
    font-family: "Bebas Neue", "Oswald", sans-serif;
    fill: var(--white);
  }
  .headline { font-size: 80px; }
  .service-line { font-size: 86px; }
</style>
</head>
<body>
<svg class="contact-banner" viewBox="0 0 1564 424" preserveAspectRatio="none" role="img" aria-label="Contact us for additional insurance, risk management, compliance, and financial services.">
  <g class="banner-shape">
    <circle cx="207" cy="212" r="208"/>
    <path d="M200,4 L583,0 L540,133 L1540,133 C1505,270 1440,405 1330,420 L200,420 Z"/>
  </g>
  <path class="headline-band" d="M583,18 L1365,18 C1350,70 1330,110 1315,133 L540,133 Z"/>

  <circle class="icon-disc" cx="212" cy="212" r="165"/>
  <path class="icon-swoosh" d="M522,222 C490,300 440,370 395,415"/>

  <g class="phone-icon" transform="translate(105,95) scale(8.6)">
    <path d="M6.62 10.79c1.44 2.83 3.76 5.14 6.59 6.59l2.2-2.2c.27-.27.67-.36 1.02-.24 1.12.37 2.33.57 3.57.57.55 0 1 .45 1 1V20c0 .55-.45 1-1 1-9.39 0-17-7.61-17-17 0-.55.45-1 1-1h3.5c.55 0 1 .45 1 1 0 1.25.2 2.45.57 3.57.11.35.03.74-.25 1.02l-2.2 2.2z"/>
  </g>

  <text class="banner-text headline" x="597" y="107" textLength="328" lengthAdjust="spacingAndGlyphs">CONTACT US</text>
  <text class="banner-text service-line" x="597" y="229" textLength="686" lengthAdjust="spacingAndGlyphs">FOR ADDITIONAL INSURANCE,</text>
  <text class="banner-text service-line" x="597" y="306" textLength="835" lengthAdjust="spacingAndGlyphs">RISK MANAGEMENT, COMPLIANCE,</text>
  <text class="banner-text service-line" x="597" y="385" textLength="625" lengthAdjust="spacingAndGlyphs">AND FINANCIAL SERVICES.</text>
</svg>
</body>
</html>
```